Bright Lantern Way (BLWY) Business Card - company with a mission

Note* The file attached... orange with "Bright Lantern WAY" (in CAPS) is our logo. I am also open to having the text "bright lantern way" OUTSIDE the orange round logo for business card (so yes, you may take the text out).

The info: (the following info are separate. So either you can use Marcus or Renata for now, but that will be 2 separate cards, not together in one card. Thanks!!

Marcus T Delvin
202.555.0137
marcus@brightlanternway.example
Managing Partner

Renata P Osk
202.555.0184
renata@brightlanternway.example
Managing Partner

Our website: www.brightlanternway.example

BLWY LLC stands for Bright Lantern Way (non profit arm is called lantern glow foundation)—our business is based out of New York City and has a non-profit arm where for every bar of soap you purchase, we donate a bar (don’t want any designs that limits us to only soap). Currently working with South Africa. We want the focus to be organic/natural soap with a mission.

Looking for a clean, fresh design.

Industry/Entity Type

Non-Profit

Requirements
Must have
• Clean, fresh, refreshing. Design should not be too busy.

```html
<!DOCTYPE html>
<html lang="en">
<head>
<meta charset="UTF-8">
<title>Bright Lantern Way — Business Card</title>
<link href="https://fonts.googleapis.com/css2?family=Fira+Sans:wght@400;500;600;700&display=swap" rel="stylesheet">
<style>
  :root {
    --stage: #2a2a2a;
    --paper: #f7f1e6;
    --peach: #f9d3ab;
    --orange: #f5ab6b;
    --green: #74c455;
    --brown: #c88a4c;
    --ink-soft: #b07a45;
  }
  * { box-sizing: border-box; margin: 0; padding: 0; }
  html, body {
    width: 1200px; height: 1000px; overflow: hidden;
    background: var(--stage);
    font-family: "Fira Sans", sans-serif;
  }
  .sheet {
    position: relative; width: 1200px; height: 1000px;
    display: flex; flex-direction: column; align-items: center; justify-content: center; gap: 60px;
  }
  .card {
    position: relative; width: 700px; height: 400px;
    background: var(--paper); overflow: hidden;
    box-shadow: 0 10px 30px rgba(0,0,0,.35);
  }
  /* front */
  .front .halo {
    position: absolute; left: 420px; top: -180px;
    width: 420px; height: 420px; border-radius: 50%;
    background: var(--peach);
  }
  .band { position: absolute; background: var(--green); }
  .front .band { left: 0; right: 0; top: 292px; height: 48px; }
  .front .mark {
    position: absolute; left: 30px; top: 258px;
    width: 112px; height: 112px; border-radius: 50%;
    background: var(--orange); border: 5px solid var(--paper);
  }
  .front .details { position: absolute; left: 160px; top: 92px; }
  .company { color: var(--brown); font-weight: 600; font-size: 30px; line-height: 1; }
  .name {
    display: inline-block; margin: 14px 0 0 40px;
    color: var(--green); font-weight: 700; font-size: 30px; line-height: 1.05;
    border-bottom: 3px solid var(--green);
  }
  .role { margin-left: 40px; margin-top: 4px; color: var(--green); font-weight: 600; font-size: 19px; letter-spacing: .5px; }
  .contacts { list-style: none; margin: 12px 0 0 60px; color: var(--ink-soft); font-size: 18px; line-height: 1.45; }
  .contacts li { display: flex; align-items: center; gap: 10px; }
  .contacts svg { width: 13px; height: 13px; flex: none; }
  /* back */
  .back .band { top: 0; bottom: 0; left: 80px; width: 50px; }
  .back .mark {
    position: absolute; left: 360px; top: 70px;
    width: 180px; height: 180px; border-radius: 50%;
    background: var(--orange);
  }
  .back .site {
    position: absolute; left: 175px; top: 300px;
    color: var(--green); font-weight: 700; font-size: 30px;
    border-bottom: 3px solid var(--green); padding-bottom: 2px;
  }
</style>
</head>
<body>
<main class="sheet">
  <section class="card front" aria-label="Business card front">
    <div class="halo" role="img" aria-label="Large soft peach circle, brand emblem area"></div>
    <div class="band"></div>
    <div class="mark" role="img" aria-label="Orange round brand emblem"></div>
    <div class="details">
      <p class="company">Bright Lantern WAY</p>
      <p class="name">Marcus T Delvin</p>
      <p class="role">Managing Partner</p>
      <ul class="contacts">
        <li><svg viewBox="0 0 12 12"><rect x="3" y="0.5" width="6" height="11" rx="1" fill="none" stroke="currentColor" stroke-width="1.2"/></svg>202.555.0137</li>
        <li><svg viewBox="0 0 12 12"><rect x="0.5" y="2" width="11" height="8" fill="currentColor"/><path d="M1 2.5 L6 6.5 L11 2.5" stroke="#f7f1e6" stroke-width="1.1" fill="none"/></svg>marcus@brightlanternway.example</li>
        <li><svg viewBox="0 0 12 12"><path d="M4 8 L8 4 M3 6 L1.5 7.5 a2 2 0 0 0 3 3 L6 9 M9 6 L10.5 4.5 a2 2 0 0 0 -3 -3 L6 3" stroke="currentColor" stroke-width="1.3" fill="none"/></svg>www.brightlanternway.example</li>
      </ul>
    </div>
  </section>

  <section class="card back" aria-label="Business card back">
    <div class="band"></div>
    <div class="mark" role="img" aria-label="Orange round brand emblem"></div>
    <p class="site">www.brightlanternway.example</p>
  </section>
</main>
</body>
</html>
```